Car Waterless Cleaner 4 in 1 (100% Natural) Clean, Shine, Protect; Water Repellent. High Eff...

We need to design labels for our Car Care & Cleaning products,
Labels on both 500 ml Bottle Spray sides (text will be provided).
5 and 10 liters Car Shampoo.

I need you to come with Car necessary images (Shining cars, Leather car seats ...)

We are a manufacturer of innovative Green Cleaning products; made with green plants and grain extract, (Leather Cleaner & Conditioner, Multi purpuses Cleaner, Car Shine Polish, car Shampoo)

Target Market(s)

Car Care & Cleaning products, Car Dealer, Car Collectors.

Logo Text

No Idea yet, lol, ;) "Auto Brisk Lantern" may be?

Font styles to use
Serif

Requirements
Must have
• Similar projects, Inoovative, Comprehencive, good expertise.

```html
<!DOCTYPE html>
<html lang="en">
<head>
<meta charset="utf-8">
<title>Auto Brisk Lantern – Car Waterless Cleaner</title>
<link href="https://fonts.googleapis.com/css2?family=Exo+2:ital,wght@0,700;0,800;1,700;1,900&display=swap" rel="stylesheet">
<style>
  :root {
    --silver-light: #f2f2f2;
    --silver-mid: #d4d4d6;
    --silver-dark: #a9a9ad;
    --green-lime: #a6c93a;
    --green-leaf: #6fa22e;
    --green-deep: #3f7a22;
    --brand-green: #2f7d2a;
    --ink: #0b0b0b;
    --white: #ffffff;
    --yellow: #f5ee14;
    --natural-green: #9fd23a;
    --panel: rgba(20, 22, 24, 0.82);
    --photo-dark: #3d3e47;
    --photo-mid: #8c8e98;
    --photo-light: #c9cad0;
  }
  * { margin: 0; padding: 0; box-sizing: border-box; }
  html, body { width: 1167px; height: 1200px; overflow: hidden; background: var(--white); }
  .label {
    position: relative; width: 1167px; height: 1200px; overflow: hidden;
    font-family: "Exo 2", "Arial Black", sans-serif;
    background: radial-gradient(ellipse at 75% 70%, #d8e23a 0%, var(--green-lime) 35%, var(--green-leaf) 70%, var(--green-deep) 100%);
  }
  .top-band {
    position: absolute; left: 0; top: 0; width: 100%; height: 200px;
    background: linear-gradient(180deg, var(--silver-light) 0%, var(--silver-mid) 100%);
  }
  .brand {
    position: absolute; top: 58px; left: 0; width: 100%;
    display: flex; justify-content: center; align-items: center; gap: 16px;
  }
  .brand-dot { width: 30px; height: 30px; border-radius: 50%; background: var(--brand-green); }
  .brand-name { font-weight: 800; font-size: 52px; color: var(--brand-green); letter-spacing: 0.5px; }
  .title-band {
    position: absolute; left: 0; top: 198px; width: 100%; height: 265px;
    background: linear-gradient(90deg, var(--green-lime) 0%, #9cc43a 50%, var(--green-leaf) 100%);
  }
  .title {
    position: absolute; left: 0; top: 205px; width: 100%; text-align: center;
    font-style: italic; font-weight: 900; font-size: 118px; line-height: 112px;
    color: var(--ink); text-transform: uppercase; letter-spacing: 2px;
    -webkit-text-stroke: 14px var(--white); paint-order: stroke fill;
    text-shadow: 4px 6px 6px rgba(0,0,0,0.35);
  }
  .scene { position: absolute; left: 0; top: 460px; }
  .claim-panel {
    position: absolute; left: 604px; top: 480px; width: 516px; height: 162px;
    background: var(--panel); border: 3px solid rgba(255,255,255,0.25); border-radius: 10px;
    text-align: center; font-style: italic; font-weight: 900;
  }
  .claim-main { color: var(--yellow); font-size: 78px; line-height: 84px; margin-top: 6px; }
  .claim-sub { color: var(--natural-green); font-size: 49px; line-height: 56px; }
  .features { position: absolute; left: 598px; top: 898px; width: 569px; list-style: none; }
  .feature {
    position: relative; height: 64px; margin-bottom: 21px;
    background: var(--ink); border-radius: 32px 0 0 32px;
  }
  .feature-icon {
    position: absolute; left: -4px; top: -8px; width: 80px; height: 80px; border-radius: 50%;
    background: var(--ink); border: 3px solid rgba(255,255,255,0.12);
    display: flex; align-items: center; justify-content: center;
  }
  .feature-text {
    position: absolute; left: 202px; top: 2px;
    color: var(--white); font-style: italic; font-weight: 700; font-size: 52px; line-height: 58px;
  }
  .volume {
    position: absolute; left: 117px; top: 1062px;
    font-weight: 800; font-size: 48px; color: var(--ink); letter-spacing: 1px;
  }
</style>
</head>
<body>
<main class="label">
  <header class="top-band">
    <div class="brand"><span class="brand-dot"></span><span class="brand-name">Auto Brisk Lantern</span></div>
  </header>

  <section class="title-band"></section>
  <h1 class="title">Car Waterless<br>Cleaner</h1>

  <svg class="scene" width="1167" height="500" viewBox="0 0 1167 500" aria-hidden="false">
    <defs>
      <linearGradient id="car-tone" x1="0" y1="0" x2="1" y2="1">
        <stop offset="0" stop-color="var(--photo-dark)"/>
        <stop offset="0.45" stop-color="var(--photo-mid)"/>
        <stop offset="0.75" stop-color="var(--photo-light)"/>
        <stop offset="1" stop-color="var(--photo-mid)"/>
      </linearGradient>
      <linearGradient id="swoosh-tone" x1="0" y1="0" x2="1" y2="0">
        <stop offset="0" stop-color="var(--silver-dark)"/>
        <stop offset="0.5" stop-color="var(--silver-light)"/>
        <stop offset="1" stop-color="var(--silver-mid)"/>
      </linearGradient>
    </defs>
    <path d="M0 0 H1050 V170 C900 260 650 360 300 420 C180 440 80 445 0 445 Z" fill="url(#swoosh-tone)"/>
    <path role="img" aria-label="Photo of a polished silver sports car with sparkling highlights"
          d="M0 0 H1050 V140 C900 230 650 330 300 390 C180 410 80 415 0 415 Z" fill="url(#car-tone)"/>
  </svg>

  <div class="claim-panel">
    <div class="claim-main">4 IN 1</div>
    <div class="claim-sub">100% NATURAL</div>
  </div>

  <ul class="features">
    <li class="feature">
      <span class="feature-icon">
        <svg width="44" height="44" viewBox="0 0 44 44"><path d="M6 30 C10 20 18 14 28 12 L38 10 L34 20 L24 24 L30 32 L18 36 C12 36 8 34 6 30 Z" fill="var(--white)"/></svg>
      </span>
      <span class="feature-text">clean</span>
    </li>
    <li class="feature">
      <span class="feature-icon">
        <svg width="44" height="44" viewBox="0 0 44 44"><path d="M16 8 L19 20 L31 23 L19 26 L16 38 L13 26 L1 23 L13 20 Z M33 4 L35 10 L41 12 L35 14 L33 20 L31 14 L25 12 L31 10 Z" fill="var(--white)"/></svg>
      </span>
      <span class="feature-text">shine</span>
    </li>
    <li class="feature">
      <span class="feature-icon">
        <svg width="44" height="44" viewBox="0 0 44 44"><path d="M22 4 L38 10 V22 C38 31 31 37 22 41 C13 37 6 31 6 22 V10 Z" fill="none" stroke="var(--white)" stroke-width="3.5" stroke-linejoin="round"/><path d="M14 22 L20 28 L30 16" fill="none" stroke="var(--white)" stroke-width="3.5" stroke-linecap="round" stroke-linejoin="round"/></svg>
      </span>
      <span class="feature-text">protect</span>
    </li>
  </ul>

  <p class="volume">5 LITRE</p>
</main>
</body>
</html>
```